Business Card, Stationary, Fax Cover, and Email Signature
Telvar Capital
Professional
Derek Hollow
President/Founder
418 Bramble Creek Lane, Suite 327
Ashcombe, NV 89990
dhollow@telvarcapital.example
www.TelvarCapital.example
Credit Repair - Credit Restoration - Credit Education ( Centered Top)
Legally And Ethically Remove Derogatory Items From Your Credit Report (Bullet Point)
Help Establish New Positive Trade Lines
(Bullet Point)
Learn How To Maintain And Increase Your Credit Score (Bullet Point)
www.TelvarCapital.example (Centered Bottom)

```html
<!DOCTYPE html>
<html lang="en">
<head>
<meta charset="utf-8">
<title>Telvar Capital — Business Card</title>
<link href="https://fonts.googleapis.com/css2?family=Open+Sans:wght@400;600;700&display=swap" rel="stylesheet">
<style>
  :root {
    --backdrop: #5b5d61;
    --card: #ffffff;
    --ink: #3a3a3a;
    --navy: #1f3f8f;
    --blue: #1c6fd0;
    --blue-light: #4fa3ee;
    --grey-band: #b9bcc1;
    --divider: #c9ccd1;
  }
  * { box-sizing: border-box; margin: 0; padding: 0; }
  html, body { width: 1200px; height: 852px; overflow: hidden; }
  body {
    background: var(--backdrop);
    font-family: "Open Sans", Arial, sans-serif;
    color: var(--ink);
    position: relative;
  }
  .card {
    position: absolute;
    width: 540px;
    height: 308px;
    background: var(--card);
    border-radius: 16px;
    overflow: hidden;
  }
  .card--front { left: 90px; top: 90px; }
  .card--alt { left: 570px; top: 460px; }
  .card__wave { position: absolute; left: 0; bottom: 0; width: 540px; height: 70px; }

  .brand { position: absolute; display: flex; align-items: center; gap: 12px; }
  .brand__dot { width: 44px; height: 44px; border-radius: 50%; background: var(--blue); flex: none; }
  .brand__name { font-weight: 600; font-size: 30px; color: var(--navy); line-height: 1.05; letter-spacing: 0.5px; white-space: nowrap; }

  .person { position: absolute; font-size: 13px; line-height: 1.45; }
  .person__name { font-weight: 700; font-size: 17px; color: var(--navy); }

  .divider { position: absolute; width: 1px; background: var(--divider); }

  .contacts { position: absolute; list-style: none; font-size: 12.5px; line-height: 1.75; }
  .contacts li { display: flex; align-items: center; gap: 8px; white-space: nowrap; }
  .contacts svg { width: 11px; height: 11px; fill: var(--blue); flex: none; }

  /* front layout */
  .card--front .brand { left: 40px; top: 40px; }
  .card--front .person { left: 40px; top: 134px; text-align: right; width: 200px; }
  .card--front .divider { left: 256px; top: 136px; height: 104px; }
  .card--front .contacts { left: 274px; top: 130px; }

  /* alternate layout */
  .card--alt .brand { left: 34px; top: 118px; }
  .card--alt .brand__name { font-size: 26px; }
  .card--alt .divider { left: 276px; top: 26px; height: 214px; }
  .card--alt .person { left: 296px; top: 22px; }
  .card--alt .contacts { left: 296px; top: 130px; }
</style>
</head>
<body>

<svg width="0" height="0" style="position:absolute" aria-hidden="true">
  <symbol id="icon-phone" viewBox="0 0 12 12"><path d="M2.5 1 4.5 3 3.6 4.4c.7 1.6 2.2 3.1 3.9 3.9L8.9 7.4 11 9.5 9.6 11C5 10.7 1.3 7 1 2.4Z"/></symbol>
  <symbol id="icon-mobile" viewBox="0 0 12 12"><rect x="3" y="0.5" width="6" height="11" rx="1.2"/></symbol>
  <symbol id="icon-fax" viewBox="0 0 12 12"><rect x="3" y="1" width="6" height="3"/><rect x="1" y="4.5" width="10" height="5" rx="1"/><rect x="3" y="9" width="6" height="2.5"/></symbol>
  <symbol id="icon-mail" viewBox="0 0 12 12"><path d="M1 2.5h10v7H1Zm.6.6L6 6.6l4.4-3.5Z"/></symbol>
  <symbol id="icon-web" viewBox="0 0 12 12"><circle cx="6" cy="6" r="5.2"/></symbol>
  <linearGradient id="waveBlue" x1="0" x2="1" y1="0" y2="0">
    <stop offset="0" stop-color="#1c6fd0"/>
    <stop offset="1" stop-color="#4fa3ee"/>
  </linearGradient>
</svg>

<section class="card card--front">
  <div class="brand">
    <span class="brand__dot"></span>
    <span class="brand__name">Telvar Capital</span>
  </div>
  <div class="person">
    <p class="person__name">Derek Hollow</p>
    <p>President/Founder</p>
    <p>418 Bramble Creek Lane</p>
    <p>Suite 327</p>
    <p>Ashcombe, NV 89990</p>
  </div>
  <span class="divider"></span>
  <ul class="contacts">
    <li><svg><use href="#icon-phone"/></svg>(555) 201-0142(T)</li>
    <li><svg><use href="#icon-mobile"/></svg>(555) 302-0186</li>
    <li><svg><use href="#icon-fax"/></svg>(555) 302-0179</li>
    <li><svg><use href="#icon-mail"/></svg>dhollow@telvarcapital.example</li>
    <li><svg><use href="#icon-web"/></svg>www.TelvarCapital.example</li>
  </ul>
  <svg class="card__wave" viewBox="0 0 540 70" preserveAspectRatio="none" aria-hidden="true">
    <path d="M0 34 C160 66 360 58 540 16 L540 70 L0 70Z" fill="var(--grey-band)"/>
    <path d="M0 50 C170 74 370 64 540 30 L540 70 L0 70Z" fill="url(#waveBlue)"/>
  </svg>
</section>

<section class="card card--alt">
  <div class="brand">
    <span class="brand__dot"></span>
    <span class="brand__name">Telvar Capital</span>
  </div>
  <span class="divider"></span>
  <div class="person">
    <p class="person__name">Derek Hollow</p>
    <p>President/Founder</p>
    <p>418 Bramble Creek Lane</p>
    <p>Suite 327</p>
    <p>Ashcombe, NV 89990</p>
  </div>
  <ul class="contacts">
    <li><svg><use href="#icon-phone"/></svg>(555) 201-0142(T)</li>
    <li><svg><use href="#icon-mobile"/></svg>(555) 302-0186</li>
    <li><svg><use href="#icon-fax"/></svg>(555) 302-0179</li>
    <li><svg><use href="#icon-mail"/></svg>dhollow@telvarcapital.example</li>
    <li><svg><use href="#icon-web"/></svg>www.TelvarCapital.example</li>
  </ul>
  <svg class="card__wave" viewBox="0 0 540 70" preserveAspectRatio="none" aria-hidden="true">
    <path d="M0 40 C170 52 360 44 540 18 L540 70 L0 70Z" fill="var(--grey-band)"/>
    <path d="M0 54 C170 68 370 58 540 32 L540 70 L0 70Z" fill="url(#waveBlue)"/>
  </svg>
</section>

</body>
</html>
```